Rising Side by Side A Handbook to Guide Managers and Crews Toward Greater Levels of Output

We need a book cover design for a book titled: Rising Side by Side:
A Handbook to Guide Managers and Crews Toward Greater Levels of Output
The book is intended to enhance the author's personal brand and promote the author's consulting services. The book also teaches: How To Help Leaders and Teams Reach New Heights of Performance. I would like to use the colors from the www.brindlemoorworks.example website (blue and orange). The design should communicate credibility and expertise in the topic of the book.

Target Market(s)

Municipal and Industrial and Energy Industry Team Leaders and Teams

Industry/Entity Type

water and waste water, energy, power generation, petrochmical

Requirements
Must have
• Look like a Dalbrook Ledger best seller. Look professional and appealling
Nice to have
• Sell at the airport. Executives keep in their office.
Should not have
• Do not plagiarize.

```html
<!DOCTYPE html>
<html lang="en">
<head>
<meta charset="utf-8">
<title>Rising Side by Side — Book Cover</title>
<link href="https://fonts.googleapis.com/css2?family=Oswald:wght@500;600&family=Montserrat:wght@800&display=swap" rel="stylesheet">
<style>
  :root {
    --stage: #333333;
    --paper: #ffffff;
    --paper-edge: #eeeeee;
    --orange: #f49b23;
    --navy: #163f73;
    --navy-light: #1f5a9c;
    --ink: #2a2a2a;
    --flock-dark: #3a3a3a;
  }
  * { margin: 0; padding: 0; box-sizing: border-box; }
  html, body {
    width: 1200px;
    height: 1200px;
    overflow: hidden;
    background: var(--stage);
  }
  .canvas {
    position: relative;
    width: 1200px;
    height: 1200px;
  }
  .cover {
    position: absolute;
    left: 280px;
    top: 60px;
    width: 640px;
    height: 1080px;
    background: linear-gradient(100deg, var(--paper) 0%, var(--paper) 70%, var(--paper-edge) 100%);
    overflow: hidden;
  }
  .flock {
    position: absolute;
    left: 90px;
    top: 90px;
    width: 460px;
    height: 130px;
  }
  .line {
    position: absolute;
    left: 0;
    right: 0;
    text-align: center;
    font-family: "Oswald", sans-serif;
    font-weight: 600;
    line-height: 1;
    text-transform: uppercase;
    white-space: nowrap;
  }
  .line--small {
    font-size: 27px;
    color: var(--ink);
  }
  .title-rising {
    top: 245px;
    font-size: 160px;
    color: var(--orange);
  }
  .title-side {
    top: 440px;
    font-size: 92px;
    color: var(--navy);
  }
  .kicker-handbook { top: 618px; }
  .subtitle-crews {
    top: 654px;
    font-size: 62px;
    color: var(--navy-light);
  }
  .kicker-toward { top: 730px; }
  .subtitle-output {
    top: 766px;
    font-size: 62px;
    color: var(--orange);
  }
  .divider {
    position: absolute;
    left: 60px;
    right: 60px;
    top: 565px;
    height: 30px;
    display: flex;
    align-items: center;
    gap: 14px;
  }
  .divider__rule {
    flex: 1;
    height: 3px;
    background: linear-gradient(90deg, rgba(22,63,115,0) 0%, var(--navy) 60%);
  }
  .divider__rule--right {
    background: linear-gradient(270deg, rgba(22,63,115,0) 0%, var(--navy) 60%);
  }
  .publisher {
    display: flex;
    align-items: center;
    gap: 6px;
    font-family: "Oswald", sans-serif;
    font-weight: 500;
    font-size: 15px;
    letter-spacing: 1px;
    color: var(--orange);
    text-transform: uppercase;
  }
  .publisher__mark {
    width: 10px;
    height: 10px;
    background: var(--orange);
  }
  .floor-shadow {
    position: absolute;
    left: 150px;
    width: 340px;
    top: 865px;
    height: 60px;
    background: radial-gradient(ellipse at center, rgba(0,0,0,0.14) 0%, rgba(0,0,0,0) 70%);
  }
  .author {
    position: absolute;
    left: 0;
    right: 0;
    top: 955px;
    text-align: center;
    font-family: "Montserrat", sans-serif;
    font-weight: 800;
    font-size: 34px;
    color: var(--ink);
    letter-spacing: 0.5px;
  }
</style>
</head>
<body>
  <div class="canvas">
    <div class="cover">
      <svg class="flock" viewBox="0 0 460 130" role="img" aria-label="Illustration of a flock of birds flying in an arch formation, led by an orange bird">
        <defs>
          <linearGradient id="flockTone" x1="0" y1="0" x2="1" y2="0">
            <stop offset="0" stop-color="var(--flock-dark)" stop-opacity="0.08"/>
            <stop offset="0.5" stop-color="var(--orange)" stop-opacity="0.35"/>
            <stop offset="1" stop-color="var(--flock-dark)" stop-opacity="0.08"/>
          </linearGradient>
        </defs>
        <path d="M0 125 Q230 -30 460 125 L460 115 Q230 -10 0 115 Z" fill="url(#flockTone)"/>
      </svg>

      <h1 class="line title-rising">Rising</h1>
      <div class="line title-side">Side by Side</div>

      <div class="divider">
        <span class="divider__rule"></span>
        <span class="publisher"><span class="publisher__mark"></span>Brindlemoor Works</span>
        <span class="divider__rule divider__rule--right"></span>
      </div>

      <div class="line line--small kicker-handbook">A Handbook to Guide</div>
      <h2 class="line subtitle-crews">Managers and Crews</h2>
      <div class="line line--small kicker-toward">Toward Greater</div>
      <div class="line subtitle-output">Levels of Output</div>

      <div class="floor-shadow"></div>
      <p class="author">AUTHOR NAME</p>
    </div>
  </div>
</body>
</html>
```